Marlowick community hall home page

We are building a modern, responsive website & booking system for our community hall. For this PixelForge task, we would like to receive design ideas for the home page.
There are no limits on the colours or fonts that can be used. We are looking for a modern, fresh design with a local/community feel. We don’t have a logo but we also recognise that our name is quite long! … So initials (MCH) instead of the name would be fine.
People book our community hall for a range of activities including: fitness classes, wedding receptions, birthday parties, business meetings, teaching, community events, charity fundraisers and other celebrations.
We have three main goals for the website. The first is that people can check our calendar and make a booking for an available time slot. The second is that they can read about our facilities and the prices for hiring them. The third is that people can find out about upcoming activities & events.
CTA: Book now
A button that links to a booking request form. (The form is not part of this design project)
Primary/Header navigation:
Home | Calendar | Facilities | Prices | Photos | News | Contact
Secondary/Footer navigation:
Chatterleaf | Quillcast
Login | Register | Privacy policy | Terms & conditions
Example texts (lorem ipsum etc. is also fine):
We have everything you need from a venue, whether it’s an elegant room with ample flexible space, a lavish and elegant hall for a wedding reception, a conference room that fits 125 delegates or a easy access venue to the town centre.
The hall is available for hire for wedding receptions, birthday celebrations, anniversaries, children's parties, presentations, lectures, fitness groups, and will comfortably accommodate all your guests.
This venue is well equipped with a modern kitchen, a range of audio and technical services, hearing loop, licensed bar, conference facilities, disabled access and unlimited free WiFi.
You can use this website to find out more about our rooms, equipment and the services we can offer and use the calendar to see where we have rooms available. You can also book rooms using our online booking system.
To the front of the building is a large public open grassed area across which is a row of shops. To the rear of the building is the large car park, including spaces for blue badge holders and a large enclosed cycle rack. This area also has extensive gardens, with seating and planting areas maintained by local volunteers.
The community hall is run and managed by volunteers of the Marlowick Community Organisation. Our objectives are to increase opportunities for people living in and around Pepperton.
We are passionate about being the heart of the community; caring for this community centred property and visitors are at the heart of all we do.
Where to go next
— Check when the hall is free
— Read our booking policy documents
— Make a booking reservation
Amenities
— Free WiFi
— Free car parking
— Fully equipped kitchen
— Hearing loop
Details for our most popular facilities (rooms):
Name: Main hall
Short description: A 127 square metre main hall with entrance lobby, toilets, a well-equipped kitchen and separate storage facilities. Three sets of double doors provide access to a large paved area and the adjacent playing field.
Capacity: 180 people
Price: £10-20 per hour
Links: More info | Book now
Name: Large meeting room
Short description: A delightful, spacious room with an outlook and access to the small walled garden. Ideal for meetings and small gatherings - it has its own access door and the use of a disabled W/C. We offer a reduced rate for this room when booked together with the main hall.
Capacity: 20 people
Price: £6-12 per hour
Attachments:
We have attached some photos of the hall & some (royalty free) stock images for inspiration.

```html
<!DOCTYPE html>
<html lang="en">
<head>
<meta charset="utf-8">
<title>Marlowick Community Hall</title>
<link href="https://fonts.googleapis.com/css2?family=Playfair+Display:wght@400;700&family=Montserrat:wght@400;600;700&display=swap" rel="stylesheet">
<style>
  :root {
    --ink: #0c0b0d;
    --panel: #161417;
    --purple: #5b2f63;
    --purple-light: #7c4a86;
    --purple-deep: #3a1c40;
    --gold: #f2c21b;
    --white: #ffffff;
    --muted: #b9b3bb;
    --mist: #d6d5d7;
    --charcoal: #2b2a2e;
  }
  * { box-sizing: border-box; margin: 0; padding: 0; }
  html, body { width: 795px; height: 1200px; overflow: hidden; background: var(--ink); }
  body { font-family: "Montserrat", sans-serif; color: var(--white); }
  .page { position: relative; width: 795px; height: 1200px; overflow: hidden; background: var(--ink); }

  .site-header { position: absolute; top: 0; left: 0; width: 100%; height: 48px; background: var(--ink); text-align: center; padding-top: 8px; }
  .brand-name { font-family: "Playfair Display", serif; font-size: 21px; letter-spacing: 3px; line-height: 1; }
  .brand-sub { font-size: 7px; letter-spacing: 3px; color: var(--muted); margin-top: 4px; }

  .main-nav { position: absolute; top: 48px; left: 0; width: 100%; height: 16px; background: linear-gradient(90deg, var(--purple-deep), var(--purple), var(--purple-deep)); display: flex; justify-content: center; gap: 60px; align-items: center; }
  .main-nav a { color: var(--white); text-decoration: none; font-size: 7.5px; letter-spacing: .5px; }

  .hero { position: absolute; top: 64px; left: 0; width: 100%; height: 222px; background: radial-gradient(ellipse at 50% 30%, #8fb4d8 0%, #4a5f86 30%, #2a2236 65%, #120f16 100%); }
  .hero-copy { position: absolute; left: 300px; top: 40px; width: 210px; }
  .hero-title { font-family: "Playfair Display", serif; font-size: 24px; line-height: 1.15; font-weight: 400; }
  .hero-text { font-size: 6.5px; line-height: 1.6; color: #e6e2ea; margin-top: 12px; }
  .btn-book { position: absolute; left: 348px; top: 170px; width: 100px; height: 24px; background: var(--gold); color: var(--ink); font-size: 10px; font-weight: 700; letter-spacing: 1px; display: flex; align-items: center; justify-content: center; border-radius: 3px; }

  .rail { position: absolute; top: 286px; width: 4px; height: 692px; background: var(--purple); }
  .rail-left { left: 128px; }
  .rail-right { left: 663px; }

  .feature { position: absolute; left: 132px; width: 531px; height: 172px; display: flex; }
  .feature.flip { flex-direction: row-reverse; }
  .feature-photo { width: 265px; height: 100%; }
  .feature-card { width: 266px; height: 100%; background: var(--panel); border-bottom: 6px solid var(--purple); display: flex; flex-direction: column; align-items: center; justify-content: center; text-align: left; padding: 0 40px; }
  .feature-title { font-family: "Playfair Display", serif; font-size: 13px; font-weight: 400; align-self: stretch; text-align: center; }
  .feature-text { font-size: 6.5px; line-height: 1.6; color: var(--muted); margin: 8px 0 12px; text-align: center; }
  .btn-more { width: 76px; height: 18px; background: var(--purple); font-size: 6.5px; font-weight: 600; letter-spacing: .5px; display: flex; align-items: center; justify-content: center; border-radius: 3px; }

  .events { position: absolute; top: 978px; left: 0; width: 100%; height: 135px; background: linear-gradient(180deg, #c9c8cb, var(--mist) 60%, #bfbdc2); text-align: center; padding-top: 20px; color: var(--charcoal); }
  .events-title { font-size: 20px; font-weight: 600; letter-spacing: 1px; }
  .events-text { width: 300px; margin: 8px auto 10px; font-size: 7px; line-height: 1.6; color: #4b4a4f; }
  .btn-gallery { display: inline-flex; width: 82px; height: 18px; background: var(--purple); color: var(--white); font-size: 6.5px; font-weight: 600; align-items: center; justify-content: center; border-radius: 3px; }

  .site-footer { position: absolute; top: 1113px; left: 0; width: 100%; height: 87px; background: linear-gradient(90deg, var(--purple-deep), var(--purple-light) 50%, var(--purple-deep)); text-align: center; padding-top: 30px; }
  .social { display: flex; justify-content: center; gap: 26px; font-size: 7px; color: #e2d6e5; }
  .site-url { margin-top: 12px; font-size: 8px; letter-spacing: 3px; color: #f0e8f2; }
</style>
</head>
<body>
<div class="page">
  <header class="site-header">
    <div class="brand-name">MARLOWICK</div>
    <div class="brand-sub">COMMUNITY HALL</div>
  </header>
  <nav class="main-nav">
    <a href="#">Home</a><a href="#">Calendar</a><a href="#">Facilities</a><a href="#">Prices</a><a href="#">Photos</a><a href="#">News</a><a href="#">Contact</a>
  </nav>

  <section class="hero" role="img" aria-label="Photo of a crowd celebrating at a lively event with confetti and stage lights">
    <div class="hero-copy">
      <h1 class="hero-title">The Perfect Place<br>For Your Event.</h1>
      <p class="hero-text">We have everything you need from a venue, whether it's an elegant room with ample flexible space or a lavish hall for a wedding reception.</p>
    </div>
    <div class="btn-book">BOOK NOW</div>
  </section>

  <div class="rail rail-left"></div>
  <div class="rail rail-right"></div>

  <section class="feature" style="top:290px">
    <div class="feature-photo" role="img" aria-label="Photo of a meeting room set with tables and chairs" style="background:linear-gradient(135deg,#e9eef2,#b8c3cc 60%,#6e7d8c)"></div>
    <div class="feature-card">
      <h2 class="feature-title">Lorem Ipsum Dolor</h2>
      <p class="feature-text">Sit amet consectetur adipiscing elit lorem<br>sit amet consectetur elit.</p>
      <div class="btn-more">LEARN MORE</div>
    </div>
  </section>

  <section class="feature flip" style="top:462px">
    <div class="feature-photo" role="img" aria-label="Photo of a hall laid out with round dining tables" style="background:linear-gradient(135deg,#3d3127,#8a7a62 50%,#d8cfc0)"></div>
    <div class="feature-card">
      <h2 class="feature-title">Lorem Ipsum Dolor</h2>
      <p class="feature-text">Sit amet consectetur adipiscing elit lorem<br>sit amet consectetur elit.</p>
      <div class="btn-more">LEARN MORE</div>
    </div>
  </section>

  <section class="feature" style="top:634px">
    <div class="feature-photo" role="img" aria-label="Photo of a colourful party buffet table" style="background:linear-gradient(135deg,#f3e4ec,#e7a7c4 45%,#7fb6d6)"></div>
    <div class="feature-card">
      <h2 class="feature-title">Lorem Ipsum Dolor</h2>
      <p class="feature-text">Sit amet consectetur adipiscing elit lorem<br>sit amet consectetur elit.</p>
      <div class="btn-more">LEARN MORE</div>
    </div>
  </section>

  <section class="feature flip" style="top:806px">
    <div class="feature-photo" role="img" aria-label="Photo of children playing on a yellow bouncy castle" style="background:linear-gradient(160deg,#f4f1e8,#e8c531 45%,#c79a12)"></div>
    <div class="feature-card">
      <h2 class="feature-title">Lorem Ipsum Dolor</h2>
      <p class="feature-text">Sit amet consectetur adipiscing elit lorem<br>sit amet consectetur elit.</p>
      <div class="btn-more">LEARN MORE</div>
    </div>
  </section>

  <section class="events" role="img" aria-label="Faded photo of a hall set for a past event">
    <h2 class="events-title">VIEW OUR PREVIOUS EVENTS</h2>
    <p class="events-text">Take a look back at the celebrations, classes and community gatherings our neighbours have hosted at the hall over the past year.</p>
    <div class="btn-gallery">VIEW GALLERY</div>
  </section>

  <footer class="site-footer">
    <div class="social"><span>Snapgrove</span><span>Chatterleaf</span><span>Quillcast</span></div>
    <div class="site-url">WWW.MARLOWICKHALL.COM</div>
  </footer>
</div>
</body>
</html>
```